Nimbo58.com.au Website and company image design

We are looking for an exceptional website designer / company to work with our new Australian Hosting Company

Nimbo58 is a new Cloud Hosting company launching in Australia that provides Scalable, On Demand computing resources to the Australian Market Place. Scalable, On Demand ocmputing is a nice way of saying fully scalable / redundant Virtual Private Server.

We require a full company image to be developed along with a Logo and Website. There is scope for ongoing development (preferred) for the successful candidate.

Website developement will require extensive jQuery ability (sliders for ordering etc (see: http://www.hostrix-example.com.au/virtual-dedicated-servers/253/zar_vps.html).

Please communicate directly with me to establish full website scope and request further documentation / content.

Target Market(s)

Website Designers, programmers, technicians and large companies

Industry/Entity Type

It Company

Requirements
Must have
• Slider ordering system such as http://www.hostrix-example.com.au/virtual-dedicated-servers/253/zar_vps.html

Nice to have
• CMS backend system
Should not have
• Should NOT be a monster template copy!!!

```html
<!DOCTYPE html>
<html lang="en">
<head>
<meta charset="utf-8">
<title>Nimbo58.com.au – Secure Cloud Hosting</title>
<link rel="stylesheet" href="https://fonts.googleapis.com/css2?family=Arimo:wght@400;700&family=Archivo+Black&display=swap">
<style>
:root{
  --topbar:#333333;
  --tab-active:#ffffff;
  --tab-idle:#595959;
  --header-bg:#f4f4f4;
  --nav-top:#6cc0ec;
  --nav-bottom:#3a9ad6;
  --sky-top:#5da5de;
  --sky-bottom:#2f7ccb;
  --brand-blue:#2e9ad8;
  --panel-blue:#4aa9e1;
  --panel-border:#2f8fcf;
  --heading-green:#3fb01c;
  --body-text:#666666;
  --dark-text:#333333;
  --footer-bg:#4eb0e4;
  --footer-bar:#45a5db;
  --white:#ffffff;
}
*{box-sizing:border-box;margin:0;padding:0}
html,body{width:1137px;height:1200px;overflow:hidden}
body{position:relative;background:#ffffff;font-family:"Arimo",Arial,sans-serif;color:var(--body-text)}
a{color:inherit;text-decoration:none}
.abs{position:absolute}

/* top bar */
.topbar{left:0;top:0;width:1137px;height:29px;background:var(--topbar)}
.site-tab{top:6px;height:23px;padding:0 17px;font-size:12px;line-height:23px;border-radius:2px 2px 0 0}
.site-tab.active{left:174px;background:var(--tab-active);color:var(--dark-text)}
.site-tab.idle{left:347px;background:var(--tab-idle);color:#dddddd}
.util-links{right:166px;top:0;display:flex;gap:29px;font-size:12px;line-height:29px;color:var(--white)}

/* header */
.header{left:0;top:29px;width:1137px;height:92px;background:var(--header-bg)}
.logo{left:177px;top:72px;display:flex;align-items:center;gap:8px;font-size:34px;font-weight:700;color:var(--brand-blue);letter-spacing:-0.5px}
.logo .dot{width:14px;height:14px;border-radius:50%;background:var(--brand-blue)}
.call{left:788px;top:52px}
.call-label{left:840px;top:63px;font-size:12px;color:var(--dark-text)}
.call-number{left:838px;top:78px;font-size:20px;color:#444444}

/* nav */
.nav{left:0;top:121px;width:1137px;height:34px;background:linear-gradient(var(--nav-top),var(--nav-bottom))}
.nav a{position:absolute;top:0;line-height:34px;font-size:14px;font-weight:700;color:var(--white)}

/* hero */
.hero{left:0;top:155px;width:1137px;height:273px;background:linear-gradient(160deg,#b8d6f1 0%,var(--sky-top) 35%,var(--sky-bottom) 100%)}
.hero-title{left:190px;top:229px;font-family:"Archivo Black",Arial,sans-serif;color:var(--white);line-height:1}
.hero-title .big{font-size:62px;letter-spacing:1px}
.hero-title .mid{font-size:33px;margin-top:2px}
.hero-sub{left:193px;top:326px;font-size:23px;font-weight:700;color:var(--white)}
.dots{left:311px;top:381px;display:flex;gap:6px}
.dots span{width:7px;height:7px;border-radius:50%;background:var(--white)}
.dots span.on{box-shadow:0 0 0 2px var(--sky-top),0 0 0 3px var(--white)}
.arrow{top:270px}
.devices{left:589px;top:258px;width:381px;height:202px;border-radius:6px;background:linear-gradient(#2b2b2b,#555555 60%,#8fc7ee)}

/* service tabs */
.service-tabs{left:158px;top:413px;width:820px;height:69px;background:linear-gradient(#ffffff,#e9eef2)}
.service-tab{top:413px;height:64px;font-size:14px;color:var(--dark-text);text-align:center}
.service-tab .icon{position:absolute;left:50%;margin-left:-22px;top:-16px;width:44px;height:48px;border-radius:6px}
.service-tab .label{position:absolute;left:0;right:0;top:38px}
.tab-divider{top:413px;width:2px;height:64px;background:#d4dde3}
.service-line{left:158px;top:477px;width:820px;height:5px;background:var(--brand-blue)}

/* content frame */
.frame{left:158px;top:482px;width:820px;height:518px;border-left:1px solid #e3e3e3;border-right:1px solid #e3e3e3}

.intro-title{left:180px;top:514px;font-size:21px;font-weight:700;color:var(--heading-green)}
.intro-text{left:181px;width:528px;font-size:10.4px;line-height:17.9px;text-align:justify}

.feature{top:780px;width:152px}
.feature .art{width:120px;height:92px;margin:0 auto;border-radius:8px}
.feature h3{margin-top:10px;text-align:center;font-size:18px;font-weight:700;color:var(--dark-text);line-height:1.1}
.feature h4{text-align:center;font-size:15px;font-weight:400;color:var(--dark-text)}
.feature p{margin-top:6px;font-size:10px;line-height:14.6px;text-align:justify}

/* sidebar */
.sidebar{left:737px;top:517px;width:222px;height:468px;background:var(--panel-blue);border:1px solid var(--panel-border);border-radius:3px}
.counter{left:744px;top:524px;width:208px;height:123px;border:1px solid #8ccbef;border-radius:2px;background:linear-gradient(#4fb2e8,#3a9fdc);color:var(--white);text-align:center}
.counter .num{position:absolute;left:0;right:0;top:14px;font-size:52px;font-weight:700;line-height:1}
.counter .plus{position:absolute;right:10px;top:2px;font-size:30px;font-weight:700}
.counter .small{position:absolute;left:0;right:0;top:64px;font-size:11px;letter-spacing:6px;font-weight:700}
.counter .big{position:absolute;left:0;right:0;top:75px;font-size:27px;font-weight:700}
.news-head{left:754px;top:658px;display:flex;align-items:center;gap:6px;font-size:19px;color:var(--white)}
.news-list{left:754px;top:686px;width:190px;list-style:none}
.news-list li{height:49px;padding-top:1px;padding-right:20px;font-size:12px;line-height:18px;color:var(--white);border-bottom:1px solid #7cc3ec}
.news-list li + li{padding-top:6px}
.news-list li:last-child{border-bottom:none}

/* footer */
.footer{left:0;top:1000px;width:1137px;height:161px;background:var(--footer-bg)}
.footer-col{top:1016px}
.footer-col h5{font-size:14px;font-weight:700;color:var(--white);margin-bottom:7px}
.footer-col ul{list-style:none;padding-left:5px}
.footer-col li{font-size:10.5px;line-height:17.9px;color:var(--white)}
.footer-logo{left:767px;top:1036px;display:flex;align-items:center;gap:7px;font-size:26px;font-weight:700;color:#8fcdf0}
.footer-logo .dot{width:12px;height:12px;border-radius:50%;background:#8fcdf0}
.social{left:767px;top:1080px;display:flex;gap:6px}
.social span{width:26px;height:26px;border-radius:3px;background:#9cd4f2}

.bottom-bar{left:0;top:1161px;width:1137px;height:39px;background:var(--footer-bar);border-top:1px solid #6fbfe9}
.copyright{left:166px;top:1173px;font-size:10.5px;color:var(--white)}
.legal{left:747px;top:1173px;display:flex;gap:12px;font-size:10.5px;color:var(--white)}
</style>
</head>
<body>

<div class="abs topbar"></div>
<a class="abs site-tab active" href="#">Servers &amp; Cloud Hosting</a>
<a class="abs site-tab idle" href="#">Resellers</a>
<nav class="abs util-links"><a href="#">Support</a><a href="#">FAQs</a><a href="#">Contact</a><a href="#">Login</a></nav>

<header class="abs header"></header>
<div class="abs logo"><span class="dot"></span>Nimbo58.com.au</div>
<svg class="abs call" width="44" height="56" viewBox="0 0 44 56" aria-hidden="true">
  <path d="M34 4c4 2 6 6 4 9l-5 4c-2 1-4 0-5-2l-3-3c-3 3-9 13-10 19l4 1c2 1 3 3 2 5l-3 6c-2 3-6 3-9 1C3 36 15 10 34 4z" fill="#3d8fd8"/>
  <path d="M9 45c-3 3-6 6-5 9" stroke="#6aaee3" stroke-width="1.5" fill="none" stroke-dasharray="2 2"/>
</svg>
<div class="abs call-label">NEED TO TALK?</div>
<div class="abs call-number">1.800.555.0142</div>

<nav class="abs nav">
  <a href="#" style="left:162px">Home</a>
  <a href="#" style="left:229px">Dedicated Servers</a>
  <a href="#" style="left:381px">Cloud Computing</a>
  <a href="#" style="left:532px">Managed Services</a>
  <a href="#" style="left:684px">Advantages</a>
  <a href="#" style="left:794px">About Us</a>
  <a href="#" style="left:892px">Contact Us</a>
</nav>

<section class="abs hero" role="img" aria-label="Bright blue sky with soft white clouds"></section>
<div class="abs hero-title"><div class="big">SECURE</div><div class="mid">CLOUD HOSTING</div></div>
<div class="abs hero-sub">The platform you can depent</div>
<div class="abs dots"><span></span><span></span><span class="on"></span><span></span></div>
<svg class="abs arrow" style="left:109px" width="31" height="31" viewBox="0 0 31 31" aria-label="Previous slide" role="img">
  <circle cx="15.5" cy="15.5" r="15" fill="#ffffff"/>
  <path d="M22 15.5H11M15 10.5l-5 5 5 5" stroke="#7a8a96" stroke-width="3" fill="none" stroke-linecap="round" stroke-linejoin="round"/>
</svg>
<svg class="abs arrow" style="left:993px" width="31" height="31" viewBox="0 0 31 31" aria-label="Next slide" role="img">
  <circle cx="15.5" cy="15.5" r="15" fill="#ffffff"/>
  <path d="M9 15.5h11M16 10.5l5 5-5 5" stroke="#2c6fb0" stroke-width="3" fill="none" stroke-linecap="round" stroke-linejoin="round"/>
</svg>

<div class="abs service-tabs"></div>
<div class="abs service-tab" style="left:158px;width:126px"><div class="icon" role="img" aria-label="Cloud storage drive icon" style="background:linear-gradient(#f2f2f2,#e59ce6)"></div><div class="label">Cloud Hosting</div></div>
<div class="abs tab-divider" style="left:284px"></div>
<div class="abs service-tab" style="left:286px;width:140px"><div class="icon" role="img" aria-label="Server rack icon" style="background:linear-gradient(#5a5a5a,#222222)"></div><div class="label">Managed hosting</div></div>
<div class="abs tab-divider" style="left:426px"></div>
<div class="abs service-tab" style="left:428px;width:148px"><div class="icon" role="img" aria-label="Hard drive with network icon" style="background:linear-gradient(#e6e6e6,#9a9a9a)"></div><div class="label">Server Management</div></div>
<div class="abs devices" role="img" aria-label="Laptop, tablet and phone with a cloud and binary code"></div>
<div class="abs service-line"></div>

<div class="abs frame"></div>

<h1 class="abs intro-title">Lorem Ipsum is simply dummy text</h1>
<p class="abs intro-text" style="top:548px">Lorem Ipsum is simply dummy text of the printing and typesetting industry. Lorem Ipsum has been the industry's standard dummy text ever since the 1500s, when an unknown printer took a galley of type and scrambled it to make a type specimen book. It has survived not only five centuries, but also the leap into electronic typesetting, remaining essentially unchanged. It was popularised in the 1960s with the release of Typemark sheets containing Lorem Ipsum passages, and more recently with desktop</p>
<p class="abs intro-text" style="top:655px">Publishing software like Quillon PageForge including versions of Lorem Ipsum.Lorem Ipsum is simply dummy text of the printing and typesetting industry. Lorem Ipsum has been the industry's standard dummy text ever since the 1500s, when an unknown printer took a galley of type and scrambled it to make a type specimen book. It has survived not only five centuries, but also the leap into electronic typesetting, remaining essentially unchanged. It was popularised in the 1960s with the release of Typemark sheets containing Lorem Ipsum passages, and more recently with desktop publishing software like Quillon PageForge including versions of Lorem Ipsum.</p>

<article class="abs feature" style="left:184px">
  <div class="art" role="img" aria-label="Cloud with sync arrows and a monitor" style="background:radial-gradient(circle,#cfe8f8,#ffffff 75%)"></div>
  <h3>Hybrid Hosting</h3><h4>Solutions</h4>
  <p>Lorem Ipsum is simply dummy text of the printing and typesetting industry. Lorem Ipsum has been the industry</p>
</article>
<article class="abs feature" style="left:370px">
  <div class="art" role="img" aria-label="Globe surrounded by networked computers" style="background:radial-gradient(circle,#5c9ad8,#dfeaf3 60%,#ffffff 75%)"></div>
  <h3>Managed</h3><h4>Applications</h4>
  <p>Lorem Ipsum is simply dummy text of the printing and typesetting industry. Lorem Ipsum has been the industry</p>
</article>
<article class="abs feature" style="left:554px">
  <div class="art" role="img" aria-label="Globe connected to a computer mouse by cable" style="background:radial-gradient(circle,#6a9ed6,#e6eef5 55%,#ffffff 75%)"></div>
  <h3>Managed</h3><h4>Services</h4>
  <p>Lorem Ipsum is simply dummy text of the printing and typesetting industry. Lorem Ipsum has been the industry</p>
</article>

<aside class="abs sidebar"></aside>
<div class="abs counter">
  <div class="plus">+</div>
  <div class="num">10000</div>
  <div class="small">SATISFAIED</div>
  <div class="big">CUSTAMERS</div>
</div>
<div class="abs news-head">
  <svg width="16" height="16" viewBox="0 0 16 16" aria-hidden="true"><circle cx="8" cy="5" r="4" fill="#ffffff"/><path d="M0 16c0-5 4-7 8-7s8 2 8 7z" fill="#ffffff"/></svg>
  Latest news
</div>
<ul class="abs news-list">
  <li>Lorem Ipsum is simply dummy text of the printing</li>
  <li>Lorem Ipsum is simply dummy text of the printing</li>
  <li>Lorem Ipsum is simply dummy text of the printing</li>
  <li>Lorem Ipsum is simply dummy text of the printing</li>
  <li>Lorem Ipsum is simply dummy text of the printing</li>
  <li>Lorem Ipsum is simply dummy text of the printing</li>
</ul>

<footer class="abs footer"></footer>
<div class="abs footer-col" style="left:168px">
  <h5>Technical Resources</h5>
  <ul><li>The Advantage</li><li>Virtual Networking</li><li>Virtual Storage</li><li>Virtual Security</li><li>Virtualization Management</li><li>Script Automation</li></ul>
</div>
<div class="abs footer-col" style="left:355px">
  <h5 style="padding-left:5px">How To Get It</h5>
  <ul><li>Download Free Trial</li><li>Contact Sales</li><li>Find a Partner</li><li>Buy Cloud</li><li>Get Volume Discount</li></ul>
</div>
<div class="abs footer-col" style="left:520px">
  <h5 style="padding-left:5px">Get Support</h5>
  <ul><li>File a Support Request</li><li>Downloads &amp; Patches</li><li>Product Support Centers</li><li>Manage Licenses</li><li>Search the Knowledge Base</li></ul>
</div>
<div class="abs footer-logo"><span class="dot"></span>Nimbo58.com.au</div>
<div class="abs social" aria-label="Social links"><span></span><span></span><span></span><span></span><span></span></div>

<div class="abs bottom-bar"></div>
<div class="abs copyright">Copyright © 2012 Nimbo58. All rights reserved.</div>
<nav class="abs legal"><a href="#">Contact Us</a><a href="#">Terms of Use</a><a href="#">Privacy</a></nav>

</body>
</html>
```